Quorlan Visit cards serious but not sad

Hello, I'd like to design my visit cards with the logo Quorlan (attached) the following information: Name: Mathis Deloraux Title: Mobile Director: 33 (0) 6 28 40 13 85 Phone: 33 (0) 4 71 86 52 09 e-mail: mathis.deloraux@quorlan-advisory.example address: 17 Rue Anatole Berrin 92400 Courbevoie This visit will be used on the banking institutions and Quorlan is a consulting firm. I do not want to have dark background.

Target Market(s)

banks

Contact Information for Business Card

Name : Mathis Deloraux
Title : Director
mobile : +33(0)6 28 40 13 85
Phone : +33(0)4 71 86 52 09
e-mail: mathis.deloraux@quorlan-advisory.example
adresse : 17 Rue anatole Berrin 92400 Courbevoie

Requirements
Nice to have
• serious but not sad

```html
<!DOCTYPE html>
<html lang="fr">
<head>
<meta charset="utf-8">
<title>Quorlan – Business cards</title>
<link href="https://fonts.googleapis.com/css2?family=Lato:wght@400;700;900&display=swap" rel="stylesheet">
<style>
  :root {
    --brand-blue: #1774bd;
    --card-white: #ececec;
    --ink: #3a3a3a;
    --rule: #b9b9b9;
    --backdrop: #262626;
  }
  * { margin: 0; padding: 0; box-sizing: border-box; }
  html, body { width: 1200px; height: 900px; overflow: hidden; }
  body {
    background: var(--backdrop);
    font-family: "Lato", "Helvetica Neue", Arial, sans-serif;
    position: relative;
  }
  .card {
    position: absolute;
    left: 290px;
    width: 620px;
    height: 355px;
    border-radius: 28px;
    overflow: hidden;
  }
  .card--front { top: 70px; background: var(--brand-blue); }
  .card--back  { top: 475px; background: var(--card-white); color: var(--ink); }

  .brand {
    position: absolute;
    display: flex;
    align-items: center;
    gap: 10px;
  }
  .brand__dot { border-radius: 50%; flex: none; }
  .brand__name { font-weight: 700; line-height: 1; letter-spacing: 1px; }

  .card--front .brand { left: 50%; top: 50%; transform: translate(-50%, -50%); }
  .card--front .brand__dot { width: 92px; height: 92px; background: #fff; }
  .card--front .brand__name { color: #fff; font-size: 62px; }

  .card--back .brand { left: 238px; top: 42px; }
  .card--back .brand__dot { width: 78px; height: 78px; background: var(--brand-blue); }
  .card--back .brand__name { color: var(--brand-blue); font-size: 52px; }

  .rule { position: absolute; height: 1px; background: var(--rule); }
  .rule--logo { left: 238px; right: 30px; top: 138px; }
  .rule--name { left: 38px; width: 330px; top: 232px; }

  .address {
    position: absolute;
    right: 34px;
    top: 158px;
    text-align: right;
    font-size: 17px;
    font-style: normal;
    line-height: 1.3;
  }
  .person { position: absolute; left: 38px; top: 202px; }
  .person__name {
    color: var(--brand-blue);
    font-weight: 900;
    font-size: 20px;
    letter-spacing: 0.5px;
    text-transform: uppercase;
  }
  .person__title { font-size: 17px; margin-top: 8px; }

  .contacts {
    position: absolute;
    left: 38px;
    top: 270px;
    list-style: none;
    font-size: 18px;
    line-height: 1.3;
  }
  .contacts li { display: flex; align-items: center; gap: 8px; }
  .contacts svg { width: 15px; height: 15px; fill: var(--brand-blue); flex: none; }
</style>
</head>
<body>

<section class="card card--front" aria-label="Card front">
  <div class="brand">
    <span class="brand__dot"></span>
    <span class="brand__name">quorlan</span>
  </div>
</section>

<section class="card card--back" aria-label="Card back">
  <div class="brand">
    <span class="brand__dot"></span>
    <span class="brand__name">quorlan</span>
  </div>
  <div class="rule rule--logo"></div>

  <address class="address">
    17 Rue anatole Berrin<br>75990 Varenne-Lisle
  </address>

  <div class="person">
    <div class="person__name">Mathis Deloraux</div>
    <div class="person__title">Director</div>
  </div>
  <div class="rule rule--name"></div>

  <ul class="contacts">
    <li>
      <svg viewBox="0 0 16 16" aria-hidden="true"><path d="M4 1h8a1 1 0 0 1 1 1v12a1 1 0 0 1-1 1H4a1 1 0 0 1-1-1V2a1 1 0 0 1 1-1zm1 2v9h6V3zm3 10a.8.8 0 1 0 0 .01z"/></svg>
      +33(0)6 28 40 13 85
    </li>
    <li>
      <svg viewBox="0 0 16 16" aria-hidden="true"><path d="M2 5c0-2 3-3 6-3s6 1 6 3v1h-3V5H5v1H2zm2 2h8l2 7H2zm4 2a2 2 0 1 0 0 4 2 2 0 0 0 0-4z"/></svg>
      +33(0)4 71 86 52 09
    </li>
    <li>
      <svg viewBox="0 0 16 16" aria-hidden="true"><path d="M1 3h14v10H1zm1.5 1.2L8 8.5l5.5-4.3z"/></svg>
      mathis.deloraux@quorlan-advisory.example
    </li>
  </ul>
</section>

</body>
</html>
```